Morvena Aesthetics Skin Care Flyer

8 1/2" x 11" three-folded brochure that will have a front panel which will show our Morvena Aesthetics logo and state that this is a Facial Menu. It might have our phone number on it and "call for appointment". The left inside flap will provide information about what we do and about the importance of facials and the rest will list services and pricing.

Kestwick Salon & Spa will not have a logo featured but it is important to show their address. Morvena Aesthetics has a newly designed logo but I am not sure how to upload it at this time. I do have a Vector file of our logo and hope to figure out the best way to make it available to all.Thank you. Added Sunday, April 26, 2015

```html
<!DOCTYPE html>
<html lang="en">
<head>
<meta charset="utf-8">
<title>Morvena Aesthetics – Facial Menu</title>
<link rel="stylesheet" href="https://fonts.googleapis.com/css2?family=Crimson+Text:wght@400;600;700&display=swap">
<style>
  :root {
    --ink-black: #0b0909;
    --panel-dark: #1d1918;
    --panel-dark-2: #2a2523;
    --gold: #d8a63c;
    --gold-band: #dba93d;
    --text-light: #f1ece6;
    --text-dark: #1a1410;
    --rule: #5b5450;
    --map-tone: #e6e2da;
  }
  * { box-sizing: border-box; margin: 0; padding: 0; }
  html, body { width: 1200px; height: 928px; overflow: hidden; background: #ffffff; }
  body { font-family: "Crimson Text", Georgia, serif; }

  .brochure {
    position: relative;
    width: 1200px;
    height: 928px;
    display: flex;
  }

  /* Left inside flap */
  .flap-about {
    width: 400px;
    height: 928px;
    display: flex;
    flex-direction: column;
  }
  .about-intro {
    height: 465px;
    background: var(--ink-black);
    color: var(--text-light);
    padding: 13px 14px 0 15px;
  }
  .about-intro p {
    font-size: 19.2px;
    line-height: 24.2px;
    text-align: justify;
    margin-bottom: 24px;
  }
  .contact-band {
    flex: 1;
    background: var(--gold-band);
    color: var(--text-dark);
    text-align: center;
    padding-top: 30px;
    position: relative;
  }
  .contact-band .address {
    font-size: 19.5px;
    line-height: 26px;
  }
  .contact-band .appointments {
    margin-top: 27px;
    font-size: 25px;
    line-height: 31px;
  }
  .location-map {
    position: absolute;
    left: 5px;
    top: 209px;
    width: 392px;
    height: 249px;
    background: linear-gradient(135deg, #b9d3e4 0%, var(--map-tone) 30%, #ede9e1 100%);
    border: 1px solid #333;
  }

  /* Services panel */
  .panel-services {
    width: 399px;
    height: 928px;
    background: linear-gradient(180deg, var(--panel-dark) 0%, var(--panel-dark-2) 100%);
    color: var(--text-light);
    padding: 10px 13px 0 15px;
    border-right: 1px solid var(--rule);
  }
  .services-title {
    color: var(--gold);
    font-weight: 700;
    font-size: 26.5px;
    line-height: 32px;
    word-spacing: 18px;
  }
  .service { margin-top: 4px; }
  .service-name {
    font-weight: 700;
    font-size: 18.5px;
    line-height: 24px;
    color: var(--gold);
    margin-bottom: 9px;
  }
  .service-name .price { color: var(--text-light); }
  .service p {
    font-size: 13.6px;
    line-height: 15.4px;
    text-align: justify;
    margin-bottom: 10px;
  }
  .products-title {
    color: var(--gold);
    font-weight: 700;
    font-size: 26.5px;
    line-height: 32px;
    margin-top: 14px;
    margin-bottom: 10px;
  }
  .panel-services .products-note {
    font-size: 13.6px;
    line-height: 15.4px;
    text-align: justify;
  }

  /* Front cover */
  .cover {
    position: relative;
    width: 401px;
    height: 928px;
    background: #1a1716;
  }
  .cover-portrait {
    position: absolute;
    inset: 0;
    background:
      radial-gradient(ellipse 70% 55% at 85% 35%, #bdb8b4 0%, #8a8480 40%, rgba(40,36,34,0) 75%),
      linear-gradient(90deg, #151212 0%, #2b2725 45%, #6d6864 100%);
  }
  .cover-brand {
    position: absolute;
    left: 0;
    right: 0;
    top: 790px;
    text-align: center;
    color: var(--gold);
    font-size: 38px;
    font-weight: 400;
    line-height: 44px;
  }
</style>
</head>
<body>
<main class="brochure">
  <section class="flap-about">
    <div class="about-intro">
      <p>No matter your skin type; dry, oily, sensitive or any kind of combination, Morvena Aesthetics has a deep cleansing facial that is designed to meet your personal needs.</p>
      <p>Your facial appointment begins with a FREE consultation so that we can initially evaluate your skin if you are a first-time client, or your progress should you already be an existing one.</p>
      <p>Our goal is for you to revel in the joy of a wonderfully healthy glow due to radiant and luminous skin as the result of an incredible treatment that will culminate in an exceptionally relaxing neck and shoulder massage.</p>
    </div>
    <div class="contact-band">
      <div class="address">Kestwick Salon &amp; Spa<br>86 Harbor Row<br>Millbrook Cove, NY 11900</div>
      <div class="appointments">Appointments:<br>631-555-0187</div>
      <div class="location-map" role="img" aria-label="Street map showing the salon location near the harbor"></div>
    </div>
  </section>

  <section class="panel-services">
    <h1 class="services-title">Facials 60&nbsp;min.</h1>

    <article class="service">
      <h2 class="service-name">Classic European <span class="price">$70.00</span></h2>
      <p>This revitalizing treatment begins with a deep cleansing, followed by gentle exfoliation to reveal smooth, glowing skin. A revitalizing masque, followed by a nutrient rich moisturizer will hydrate, protect and help restore the natural balance of your skin.</p>
    </article>

    <article class="service">
      <h2 class="service-name">Anti-Aging <span class="price">$80.00</span> + Glycolic Peel <span class="price">$20.00</span></h2>
      <p>A highly effective treatment for targeting visible signs of aging (fine lines, wrinkles, sun damage, etc.) and restoring a more youthful appearance. We utilize Vitamin C along with a peptide smoothing serum to produce desirable results. Add a glycolic peel for an even more efficient removal of dead skin layers while stimulating collagen production.</p>
    </article>

    <article class="service">
      <h2 class="service-name">Aroma Therapy <span class="price">$80.00</span></h2>
      <p>A deep cleansing and exfoliation will restore your skin’s natural radiance. The pressure point massage will stimulate blood circulation and revitalize the tissues while the wonderfully fragrant and essential oils soothe your senses and rejuvenate your skin.</p>
    </article>

    <article class="service">
      <h2 class="service-name">Acne Glycolic Exfoliation Treatment <span class="price">$95.00</span></h2>
      <p>Acne facials or deep cleansing facials are recommended for clients prone to oily or acneic skin or for those with uneven complexions. We incorporate a combination of thorough steaming, deep cleansing, facial extractions to remove pore-clogging sebum, and a healing mask and moisturizer. Salicylic and glycolic acids are aimed at managing and thwarting acne flare-ups.</p>
    </article>

    <article class="service">
      <h2 class="service-name">Sensitive Facial <span class="price">$80.00</span></h2>
      <p>For sensitive skin, this facial utilizes gentle procedures and hypoallergenic products that are appropriate for irritation-prone skin. Those with skin sensitivities should not fear the calming effects of this delicate treatment. Facials for sensitive skin can improve complexion, reduce inflammation and boost your skin’s immunity, which will help prevent future irritations.</p>
    </article>

    <h2 class="products-title">Products</h2>
    <p class="products-note">We also offer exceptional products that allow for further improvement between facials, when at home.</p>
  </section>

  <section class="cover">
    <div class="cover-portrait" role="img" aria-label="Black and white beauty portrait with glowing skin"></div>
    <div class="cover-brand">Morvena Aesthetics</div>
  </section>
</main>
</body>
</html>
```